KerrLow Farm

Need a nice simple clean double sided business card that has our logo and info on:
Kerr Low Farm
Martin & Felicity Kerr Low
kerrlowfarm@mailbarn.example
Martin: 1-780-555-0148
Felicity: 1-780-555-0193
Instagram @ kerrlow_farm

Contact Information for Business Card

Martin & Felicity Kerr Low kerrlowfarm@mailbarn.example Martin: 1-780-555-0148 Felicity: 1-780-555-0193

```html
<!DOCTYPE html>
<html lang="en">
<head>
<meta charset="UTF-8">
<title>Kerr Low Farm – Business Card</title>
<link href="https://fonts.googleapis.com/css2?family=Cinzel:wght@500&family=Marcellus&family=Montserrat:wght@400&family=Open+Sans:wght@400&display=swap" rel="stylesheet">
<style>
  :root {
    --backdrop: #e6e6e6;
    --farm-green: #609e3f;
    --harvest-orange: #eea01f;
    --card-white: #f4f4f4;
    --ink: #2f2f2f;
    --white: #ffffff;
  }
  * { margin: 0; padding: 0; box-sizing: border-box; }
  html, body {
    width: 1200px; height: 960px; overflow: hidden;
    background: var(--backdrop);
  }
  .canvas { position: relative; width: 1200px; height: 960px; }

  .card {
    position: absolute; top: 187px; width: 340px; height: 593px; overflow: hidden;
  }
  .card-front { left: 235px; background: var(--farm-green); }
  .card-back { left: 626px; background: var(--card-white); }

  /* front */
  .front-title {
    position: absolute; left: 0; top: 0;
    transform-origin: 0 0;
    white-space: nowrap;
  }
  .front-name {
    transform: translate(32px, 426px) rotate(-90deg);
    font-family: "Marcellus", serif;
    font-size: 47px; line-height: 48px; color: var(--white);
    letter-spacing: 1.6px;
  }
  .front-tagline {
    transform: translate(78px, 426px) rotate(-90deg);
    font-family: "Montserrat", sans-serif;
    font-size: 17px; line-height: 20px; color: var(--harvest-orange);
    letter-spacing: 11.3px;
  }
  .wheat-art {
    position: absolute; left: 118px; top: 170px; width: 210px; height: 423px;
    background: linear-gradient(160deg, rgba(238,160,31,0.85) 0%, rgba(238,160,31,0.55) 55%, rgba(255,255,255,0.35) 100%);
    border-radius: 100px 100px 0 0;
  }

  /* back */
  .brand-name {
    position: absolute; left: 0; width: 100%; top: 150px; text-align: center;
    font-family: "Marcellus", serif; font-size: 28px; line-height: 32px; color: var(--farm-green);
  }
  .owners {
    position: absolute; left: 0; width: 100%; top: 276px; text-align: center;
    font-family: "Cinzel", serif; font-size: 21px; line-height: 27px; font-weight: 500;
  }
  .owners .first-names { color: var(--farm-green); display: block; }
  .owners .surname { color: var(--harvest-orange); display: block; }

  .divider { position: absolute; left: 65px; width: 210px; height: 22px; }
  .contact {
    position: absolute; left: 0; width: 100%; text-align: center;
    font-family: "Open Sans", sans-serif; font-size: 14px; line-height: 20px; color: var(--ink);
  }
  .contact .person { color: var(--farm-green); }
</style>
</head>
<body>
<div class="canvas">

  <section class="card card-front">
    <div class="front-title front-name">KERR LOW FARM</div>
    <div class="front-title front-tagline">STONE MILLED FLOUR</div>
    <div class="wheat-art" role="img" aria-label="Illustration of two golden wheat stalks with white grass blades"></div>
  </section>

  <section class="card card-back">
    <div class="brand-name">KERR LOW FARM</div>

    <div class="owners">
      <span class="first-names">Martin &amp; Felicity</span>
      <span class="surname">Kerr Low</span>
    </div>

    <svg class="divider" style="top:393px" viewBox="0 0 210 22" aria-hidden="true">
      <line x1="0" y1="11" x2="93" y2="11" stroke="var(--harvest-orange)" stroke-width="1.5"/>
      <line x1="117" y1="11" x2="210" y2="11" stroke="var(--harvest-orange)" stroke-width="1.5"/>
      <circle cx="105" cy="11" r="10" fill="none" stroke="var(--harvest-orange)" stroke-width="1.5"/>
      <rect x="101" y="5" width="8" height="12" rx="1.5" fill="none" stroke="var(--harvest-orange)" stroke-width="1.3"/>
      <line x1="104" y1="15" x2="106" y2="15" stroke="var(--harvest-orange)" stroke-width="1.2"/>
    </svg>
    <div class="contact" style="top:417px">
      <span class="person">Martin</span> 1-780-555-0148<br>
      <span class="person">Felicity</span> 1-780-555-0193
    </div>

    <svg class="divider" style="top:459px" viewBox="0 0 210 22" aria-hidden="true">
      <line x1="0" y1="11" x2="93" y2="11" stroke="var(--harvest-orange)" stroke-width="1.5"/>
      <line x1="117" y1="11" x2="210" y2="11" stroke="var(--harvest-orange)" stroke-width="1.5"/>
      <circle cx="105" cy="11" r="10" fill="none" stroke="var(--harvest-orange)" stroke-width="1.5"/>
      <rect x="99" y="7" width="12" height="8" fill="none" stroke="var(--harvest-orange)" stroke-width="1.3"/>
      <polyline points="99,7 105,12 111,7" fill="none" stroke="var(--harvest-orange)" stroke-width="1.3"/>
    </svg>
    <div class="contact" style="top:480px">kerrlowfarm@mailbarn.example</div>

    <svg class="divider" style="top:505px" viewBox="0 0 210 22" aria-hidden="true">
      <line x1="0" y1="11" x2="93" y2="11" stroke="var(--harvest-orange)" stroke-width="1.5"/>
      <line x1="117" y1="11" x2="210" y2="11" stroke="var(--harvest-orange)" stroke-width="1.5"/>
      <circle cx="105" cy="11" r="10" fill="none" stroke="var(--harvest-orange)" stroke-width="1.5"/>
    </svg>
    <div class="contact" style="top:526px">@kerrlow_farm</div>
  </section>

</div>
</body>
</html>
```